Need a website setup for our new removalist business.
Our business is called Pine Harbour Removals and would like a website setup.
We don’t have a website, logo or design as of yet. Our truck is blue so something possibly that works and can incorporate the blue.

```html
<!DOCTYPE html>
<html lang="en">
<head>
<meta charset="utf-8">
<title>Pine Harbour Removals</title>
<link href="https://fonts.googleapis.com/css2?family=Poppins:wght@400;500;600;700;800&display=swap" rel="stylesheet">
<style>
:root{
  --blue:#0c4a97;
  --blue-dark:#083a78;
  --yellow:#f6b22d;
  --ink:#1b1b1b;
  --muted:#6b6b6b;
  --footer:#151515;
  --footer-text:#cfcfcf;
  --white:#ffffff;
}
*{margin:0;padding:0;box-sizing:border-box}
html,body{width:1200px;height:4990px;overflow:hidden}
body{position:relative;font-family:'Poppins',sans-serif;color:var(--ink);background:var(--white)}
.abs{position:absolute}
.btn{position:absolute;display:flex;align-items:center;justify-content:center;gap:10px;font-weight:600;font-size:17px;text-transform:uppercase;letter-spacing:.3px}
.btn-yellow{background:var(--yellow);color:var(--white)}
.btn-blue{background:var(--blue);color:var(--white)}
.arrow-ne{width:14px;height:14px}
.topbar{left:0;top:0;width:1200px;height:42px;background:var(--blue);color:var(--white);font-size:15px}
.topbar span{position:absolute;top:11px}
.social-dot{position:absolute;width:11px;height:11px;border-radius:50%;background:var(--yellow)}
.nav{left:0;top:42px;width:1200px;height:84px;background:var(--white);box-shadow:0 2px 6px rgba(0,0,0,.08)}
.brand{position:absolute;display:flex;align-items:center;gap:10px;font-weight:700;color:var(--blue);white-space:nowrap}
.brand i{display:block;background:var(--yellow)}
.menu{position:absolute;left:402px;top:40px;display:flex;gap:40px;font-size:13px;font-weight:500}
.hero{left:0;top:126px;width:1200px;height:730px;background:linear-gradient(180deg,#5b5f66 0%,#3f4349 55%,#33363b 100%)}
.hero-title{top:300px;width:1160px;text-align:center;font-size:58px;line-height:68px;font-weight:800;color:var(--white)}
.hero-text{top:450px;width:1160px;text-align:center;font-size:19px;line-height:23px;color:var(--white)}
.label{position:absolute;font-size:19px;font-weight:500}
.h2{position:absolute;font-weight:600;line-height:1.2}
.para{position:absolute;color:var(--muted);font-size:20px;line-height:24px}
.feature{position:absolute;top:1485px;width:266px;height:228px;border:1px solid #e2e2e2;border-radius:12px;background:var(--white);text-align:center;box-shadow:0 3px 8px rgba(0,0,0,.04)}
.feature .ico{width:80px;height:70px;margin:18px auto 0;border-radius:50%;background:linear-gradient(135deg,var(--yellow) 45%,#dbe6f5 45%)}
.feature h3{font-size:16px;font-weight:500;margin-top:20px}
.feature p{font-size:9.5px;color:var(--muted);text-transform:uppercase;margin:12px auto 0;width:170px;line-height:16px}
.readmore{font-size:13px;font-weight:600;color:var(--blue);display:flex;justify-content:center;align-items:center;gap:12px;margin-top:20px}
.services{left:0;top:1825px;width:1200px;height:840px;background:var(--blue)}
.svc{position:absolute;top:2035px;width:224px;height:336px;background:var(--white)}
.svc .ico{position:absolute;left:30px;top:35px;width:72px;height:60px;border-radius:50%;background:linear-gradient(135deg,#6f8fc0 50%,#cdd8ea 50%)}
.svc h3{position:absolute;left:28px;top:135px;font-size:16px;font-weight:600}
.svc p{position:absolute;left:28px;top:166px;width:172px;font-size:10px;line-height:13px;color:var(--muted)}
.svc .rm{position:absolute;left:28px;top:238px;font-size:11px;font-weight:600;color:var(--yellow);display:flex;gap:12px;align-items:center}
.step{position:absolute;left:113px;width:482px;height:72px;background:var(--white);border-radius:6px;box-shadow:0 4px 14px rgba(0,0,0,.1)}
.step .dot{position:absolute;left:32px;top:14px;width:48px;height:48px;border-radius:50%;background:var(--yellow)}
.step h4{position:absolute;left:104px;top:23px;font-size:20px;font-weight:600;white-space:nowrap}
.step p{position:absolute;left:245px;top:12px;width:200px;font-size:11px;line-height:16px;color:var(--muted)}
.tcard{position:absolute;top:3640px;width:414px;height:255px;background:var(--white);box-shadow:0 4px 20px rgba(0,0,0,.08)}
.tcard .av{position:absolute;left:25px;top:20px;width:62px;height:62px;border-radius:50%;background:#b9a48c}
.tcard .nm{position:absolute;left:103px;top:28px;font-size:13px;font-weight:600;color:var(--blue)}
.tcard .st{position:absolute;left:103px;top:48px;font-size:14px;color:var(--yellow);letter-spacing:3px}
.tcard .q{position:absolute;right:20px;top:6px;font-size:60px;font-weight:800;color:var(--blue);line-height:1}
.tcard p{position:absolute;left:30px;top:120px;width:355px;font-size:14px;line-height:17px;color:var(--muted)}
.t-arrow{position:absolute;top:3742px;width:60px;height:44px}
.contact{left:0;top:4020px;width:1200px;height:620px;background:linear-gradient(180deg,#1f4f97,#2a5aa3)}
.field{position:absolute;background:var(--white);font-size:10px;color:#9a9a9a;padding:10px 18px}
.footer{left:0;top:4600px;width:1200px;height:390px;background:var(--footer);color:var(--footer-text)}
.fcol h4{position:absolute;top:4695px;font-size:22px;font-weight:500;color:var(--white)}
.flist{position:absolute;font-size:14px;line-height:33px;color:var(--footer-text);white-space:nowrap}
.flist div{display:flex;align-items:center;gap:8px}
.flist svg{width:14px;height:12px;flex:none}
</style>
</head>
<body>

<!-- top bar -->
<div class="abs topbar">
  <svg class="abs" style="left:78px;top:15px" width="15" height="11" viewBox="0 0 15 11"><rect width="15" height="11" rx="1" fill="#f6b22d"/><path d="M0 0l7.5 6L15 0" stroke="#0c4a97" stroke-width="1.5" fill="none"/></svg>
  <span style="left:106px">info@pineharbour.test</span>
  <svg class="abs" style="left:290px;top:13px" width="15" height="15" viewBox="0 0 24 24"><path d="M6.6 10.8a15 15 0 006.6 6.6l2.2-2.2c.3-.3.7-.4 1-.2 1.1.4 2.3.6 3.6.6.6 0 1 .4 1 1V20c0 .6-.4 1-1 1A17 17 0 013 4c0-.6.4-1 1-1h3.5c.6 0 1 .4 1 1 0 1.3.2 2.5.6 3.6.1.3 0 .7-.2 1z" fill="#f6b22d"/></svg>
  <span style="left:318px">(555) 014 2290</span>
  <i class="social-dot" style="left:1068px;top:15px"></i>
  <i class="social-dot" style="left:1092px;top:15px"></i>
  <i class="social-dot" style="left:1116px;top:15px"></i>
</div>

<!-- nav -->
<div class="abs nav">
  <div class="brand" style="left:70px;top:28px;font-size:17px"><i style="width:24px;height:24px"></i>Pine Harbour Removals</div>
  <nav class="menu"><span>HOME</span><span>ABOUT</span><span>SERVICES</span><span>PRICING</span><span>TESTIMONIALS</span></nav>
  <div class="btn btn-blue" style="left:1037px;top:30px;width:108px;height:26px;font-size:10px;gap:6px">Get a quote
    <svg class="arrow-ne" style="width:9px;height:9px" viewBox="0 0 14 14"><path d="M2 12L12 2M4 2h8v8" stroke="#fff" stroke-width="2" fill="none"/></svg></div>
</div>

<!-- hero -->
<div class="abs hero" role="img" aria-label="Photo of two movers carrying cardboard boxes through a living room"></div>
<h1 class="abs hero-title" style="left:20px">Moving Every Customer<br>With Care</h1>
<p class="abs hero-text" style="left:20px">Lorem ipsum dolor sit amet, consectetuer adipiscing elit.<br>Aenean commodo ligula eget dolor.<br>Aenean massa. Cum sociis natoque penatibus et<br>magnis dis parturient montes, nascetur ridiculus mus.</p>
<div class="btn btn-yellow" style="left:428px;top:578px;width:178px;height:46px">Get a quote
  <svg class="arrow-ne" viewBox="0 0 14 14"><path d="M2 12L12 2M4 2h8v8" stroke="#fff" stroke-width="2" fill="none"/></svg></div>
<div class="btn btn-blue" style="left:620px;top:578px;width:176px;height:46px">Our services
  <svg class="arrow-ne" viewBox="0 0 14 14"><path d="M2 12L12 2M4 2h8v8" stroke="#fff" stroke-width="2" fill="none"/></svg></div>
<svg class="abs" style="left:0;top:700px" width="1200" height="160" viewBox="0 0 1200 160">
  <path d="M0 80C220 20 430 110 650 100S1000 40 1200 55V160H0Z" fill="#f6b22d"/>
  <path d="M0 62C220 10 430 95 650 88S1000 30 1200 40V70C1000 60 860 110 650 118S220 70 0 108Z" fill="#0c4a97"/>
  <path d="M0 140C250 90 450 140 700 130S1050 60 1200 68V160H0Z" fill="#fff"/>
</svg>

<!-- about -->
<div class="label" style="left:112px;top:1018px;color:var(--blue)">About Us</div>
<h2 class="h2" style="left:112px;top:1055px;font-size:40px;line-height:48px">We are Your Partner<br>to Moving Across<br>Everywhere.</h2>
<p class="para" style="left:112px;top:1218px;width:440px">LLorem ipsum dolor sit amet, consectetur adipiscing elit. Ut elit tellus, luctus nec ullamcorper mattis, pulvinar dapibus leo.</p>
<div class="btn btn-blue" style="left:112px;top:1330px;width:188px;height:46px">Get a quote
  <svg class="arrow-ne" viewBox="0 0 14 14"><path d="M2 12L12 2M4 2h8v8" stroke="#fff" stroke-width="2" fill="none"/></svg></div>
<div class="abs" style="left:683px;top:993px;width:400px;height:365px;border:6px solid var(--yellow)"></div>
<div class="abs" role="img" aria-label="Photo of a mover holding a box beside a blue removal van" style="left:605px;top:1040px;width:515px;height:290px;background:linear-gradient(180deg,#dfe7f4 0%,#4a78c8 100%)"></div>

<!-- features -->
<div class="feature" style="left:103px"><div class="ico"></div><h3>Satisfaction Guarantee</h3><p>Lorem ipsum dolor sit amet, consectetuer adipiscing elit.</p><div class="readmore">READ MORE <svg class="arrow-ne" viewBox="0 0 14 14"><path d="M2 12L12 2M4 2h8v8" stroke="#f6b22d" stroke-width="2" fill="none"/></svg></div></div>
<div class="feature" style="left:448px"><div class="ico"></div><h3>Competitive Prices</h3><p>Lorem ipsum dolor sit amet, consectetuer adipiscing elit.</p><div class="readmore">READ MORE <svg class="arrow-ne" viewBox="0 0 14 14"><path d="M2 12L12 2M4 2h8v8" stroke="#f6b22d" stroke-width="2" fill="none"/></svg></div></div>
<div class="feature" style="left:802px"><div class="ico"></div><h3>Going The Extra Mile</h3><p>Lorem ipsum dolor sit amet, consectetuer adipiscing elit.</p><div class="readmore">READ MORE <svg class="arrow-ne" viewBox="0 0 14 14"><path d="M2 12L12 2M4 2h8v8" stroke="#f6b22d" stroke-width="2" fill="none"/></svg></div></div>

<!-- services -->
<div class="abs services"></div>
<div class="label" style="left:0;width:1200px;text-align:center;top:1896px;color:var(--yellow)">What We Do</div>
<h2 class="h2" style="left:0;width:1200px;text-align:center;top:1935px;font-size:38px;color:var(--white)">Our Services</h2>
<div class="svc" style="left:121px"><div class="ico"></div><h3>Local Moving</h3><p>Lorem ipsum dolor sit amet, consectetur adipiscing elit. Ut elit tellus, luctus nec ullamcorper mattis, pulvinar dapibus leo.</p><div class="rm">READ MORE <svg class="arrow-ne" style="width:11px;height:11px" viewBox="0 0 14 14"><path d="M2 12L12 2M4 2h8v8" stroke="#f6b22d" stroke-width="2" fill="none"/></svg></div></div>
<div class="svc" style="left:370px"><div class="ico"></div><h3>Commercial Moving</h3><p>Lorem ipsum dolor sit amet, consectetur adipiscing elit. Ut elit tellus, luctus nec ullamcorper mattis, pulvinar dapibus leo.</p><div class="rm">READ MORE <svg class="arrow-ne" style="width:11px;height:11px" viewBox="0 0 14 14"><path d="M2 12L12 2M4 2h8v8" stroke="#f6b22d" stroke-width="2" fill="none"/></svg></div></div>
<div class="svc" style="left:619px"><div class="ico"></div><h3>Military Moving</h3><p>Lorem ipsum dolor sit amet, consectetur adipiscing elit. Ut elit tellus, luctus nec ullamcorper mattis, pulvinar dapibus leo.</p><div class="rm">READ MORE <svg class="arrow-ne" style="width:11px;height:11px" viewBox="0 0 14 14"><path d="M2 12L12 2M4 2h8v8" stroke="#f6b22d" stroke-width="2" fill="none"/></svg></div></div>
<div class="svc" style="left:868px"><div class="ico"></div><h3>Truck Rental</h3><p>Lorem ipsum dolor sit amet, consectetur adipiscing elit. Ut elit tellus, luctus nec ullamcorper mattis, pulvinar dapibus leo.</p><div class="rm">READ MORE <svg class="arrow-ne" style="width:11px;height:11px" viewBox="0 0 14 14"><path d="M2 12L12 2M4 2h8v8" stroke="#f6b22d" stroke-width="2" fill="none"/></svg></div></div>
<svg class="abs" style="left:38px;top:2183px" width="68" height="46" viewBox="0 0 68 46"><circle cx="40" cy="23" r="22" fill="#5b7fb8"/><path d="M62 23H6M22 7L6 23l16 16" stroke="#fff" stroke-width="5" fill="none"/></svg>
<svg class="abs" style="left:1100px;top:2183px" width="68" height="46" viewBox="0 0 68 46"><circle cx="28" cy="23" r="22" fill="#5b7fb8"/><path d="M6 23h56M46 7l16 16-16 16" stroke="#fff" stroke-width="5" fill="none"/></svg>
<div class="btn btn-yellow" style="left:500px;top:2412px;width:190px;height:45px">Get a quote
  <svg class="arrow-ne" viewBox="0 0 14 14"><path d="M2 12L12 2M4 2h8v8" stroke="#fff" stroke-width="2" fill="none"/></svg></div>
<svg class="abs" style="left:0;top:2500px" width="1200" height="170" viewBox="0 0 1200 170">
  <path d="M0 110C220 60 380 50 560 60S950 90 1200 20V80C960 130 760 110 560 110S200 150 0 160Z" fill="#f6b22d"/>
  <path d="M0 150C220 90 380 80 560 90S950 110 1200 60V170H0Z" fill="#fff"/>
</svg>

<!-- process -->
<div class="step" style="top:2812px;transform:rotate(-3deg)"><div class="dot"></div><h4>01. Plan</h4><p>Use our planning timeline and moving tips to prepare for a smooth move.</p></div>
<div class="step" style="top:2940px;transform:rotate(1deg)"><div class="dot"></div><h4>02. Pack</h4><p>Use our planning timeline and moving tips to prepare for a smooth move.</p></div>
<div class="step" style="top:3062px;transform:rotate(-3deg)"><div class="dot"></div><h4>03. Load</h4><p>Use our planning timeline and moving tips to prepare for a smooth move.</p></div>
<div class="step" style="top:3188px;transform:rotate(1deg)"><div class="dot"></div><h4>04. Delivery</h4><p>Use our planning timeline and moving tips to prepare for a smooth move.</p></div>
<div class="label" style="left:660px;top:2803px;color:var(--blue)">Our Process</div>
<h2 class="h2" style="left:660px;top:2843px;font-size:40px;line-height:48px">Your Stress-Free Move<br>&nbsp;in 4 Simple Steps</h2>
<p class="para" style="left:668px;top:2963px;width:440px">LLorem ipsum dolor sit amet, consectetur adipiscing elit. Ut elit tellus, luctus nec ullamcorper mattis, pulvinar dapibus leo.</p>

<!-- testimonials -->
<div class="label" style="left:0;width:1200px;text-align:center;top:3437px;color:var(--blue)">Testimonials</div>
<h2 class="h2" style="left:0;width:1200px;text-align:center;top:3475px;font-size:38px">What Client Says</h2>
<div class="tcard" style="left:153px"><div class="av" role="img" aria-label="Client portrait photo"></div><div class="nm">Liam R.</div><div class="st">★★★★★</div><div class="q">”</div><p>Lorem ipsum dolor sit amet, consectetuer adipiscing elit. Aenean commodo ligula eget dolor.Aenean massa. Cum sociis natoque penatibus et magnis dis parturient montes, nascetur ridiculus mus.</p></div>
<div class="tcard" style="left:622px"><div class="av" role="img" aria-label="Client portrait photo"></div><div class="nm">Liam R.</div><div class="st">★★★★★</div><div class="q">”</div><p>Lorem ipsum dolor sit amet, consectetuer adipiscing elit. Aenean commodo ligula eget dolor.Aenean massa. Cum sociis natoque penatibus et magnis dis parturient montes, nascetur ridiculus mus.</p></div>
<svg class="t-arrow" style="left:60px" viewBox="0 0 60 44"><circle cx="38" cy="22" r="20" fill="#fbe3b0"/><path d="M56 22H6M20 8L6 22l14 14" stroke="#0c4a97" stroke-width="4" fill="none"/></svg>
<svg class="t-arrow" style="left:1082px" viewBox="0 0 60 44"><circle cx="22" cy="22" r="20" fill="#fbe3b0"/><path d="M4 22h50M40 8l14 14-14 14" stroke="#0c4a97" stroke-width="4" fill="none"/></svg>

<!-- contact -->
<div class="abs contact" role="img" aria-label="Blue-tinted photo of a home interior with a mover carrying a cardboard box on the right"></div>
<div class="label" style="left:143px;top:4100px;color:var(--yellow)">Quote</div>
<h2 class="h2" style="left:140px;top:4140px;font-size:38px;color:var(--white)">Get in Touch</h2>
<div class="field" style="left:143px;top:4218px;width:190px;height:38px">Name</div>
<div class="field" style="left:347px;top:4218px;width:190px;height:38px">EMail</div>
<div class="field" style="left:553px;top:4218px;width:190px;height:38px">Phone</div>
<div class="field" style="left:138px;top:4275px;width:610px;height:98px">Message</div>
<div class="btn btn-yellow" style="left:143px;top:4400px;width:180px;height:44px">Get a quote
  <svg class="arrow-ne" viewBox="0 0 14 14"><path d="M2 12L12 2M4 2h8v8" stroke="#fff" stroke-width="2" fill="none"/></svg></div>

<!-- footer -->
<div class="abs footer"></div>
<svg class="abs" style="left:0;top:4520px" width="1200" height="140" viewBox="0 0 1200 140">
  <path d="M0 40C240 110 560 80 800 70S1100 80 1200 30V140H0Z" fill="#f6b22d"/>
  <path d="M0 70C240 130 560 100 800 92S1100 95 1200 60V140H0Z" fill="#151515"/>
</svg>
<div class="brand" style="left:100px;top:4708px;font-size:25px;color:var(--white)"><i style="width:36px;height:36px"></i>Pine Harbour Removals</div>
<p class="abs" style="left:100px;top:4795px;width:310px;font-size:13px;line-height:20px;color:var(--footer-text)">Lorem ipsum dolor sit amet, consectetuer adipiscing elit. Aenean commodo ligula eget dolor. Aenean massa.</p>
<i class="social-dot" style="left:102px;top:4870px;width:16px;height:16px"></i>
<i class="social-dot" style="left:132px;top:4870px;width:16px;height:16px"></i>
<i class="social-dot" style="left:162px;top:4870px;width:16px;height:16px"></i>
<div class="fcol"><h4 style="left:500px">Quick Links</h4><h4 style="left:720px">Services</h4><h4 style="left:947px">Contact us</h4></div>
<div class="flist" style="left:508px;top:4745px">
  <div><svg viewBox="0 0 14 12"><path d="M0 6h12M7 1l5 5-5 5" stroke="#f6b22d" stroke-width="2" fill="none"/></svg>Home</div>
  <div><svg viewBox="0 0 14 12"><path d="M0 6h12M7 1l5 5-5 5" stroke="#f6b22d" stroke-width="2" fill="none"/></svg>About</div>
  <div><svg viewBox="0 0 14 12"><path d="M0 6h12M7 1l5 5-5 5" stroke="#f6b22d" stroke-width="2" fill="none"/></svg>Services</div>
  <div><svg viewBox="0 0 14 12"><path d="M0 6h12M7 1l5 5-5 5" stroke="#f6b22d" stroke-width="2" fill="none"/></svg>Pricing</div>
  <div><svg viewBox="0 0 14 12"><path d="M0 6h12M7 1l5 5-5 5" stroke="#f6b22d" stroke-width="2" fill="none"/></svg>Contact</div>
</div>
<div class="flist" style="left:728px;top:4750px">
  <div><svg viewBox="0 0 14 12"><path d="M0 6h12M7 1l5 5-5 5" stroke="#f6b22d" stroke-width="2" fill="none"/></svg>Local Moving</div>
  <div><svg viewBox="0 0 14 12"><path d="M0 6h12M7 1l5 5-5 5" stroke="#f6b22d" stroke-width="2" fill="none"/></svg>Commercial Moving</div>
  <div><svg viewBox="0 0 14 12"><path d="M0 6h12M7 1l5 5-5 5" stroke="#f6b22d" stroke-width="2" fill="none"/></svg>Military Moving</div>
  <div><svg viewBox="0 0 14 12"><path d="M0 6h12M7 1l5 5-5 5" stroke="#f6b22d" stroke-width="2" fill="none"/></svg>StorageSolutions</div>
  <div><svg viewBox="0 0 14 12"><path d="M0 6h12M7 1l5 5-5 5" stroke="#f6b22d" stroke-width="2" fill="none"/></svg>Truck Rental</div>
</div>
<div class="flist" style="left:952px;top:4750px;font-size:13px">
  <div><svg viewBox="0 0 24 24"><path d="M6.6 10.8a15 15 0 006.6 6.6l2.2-2.2c.3-.3.7-.4 1-.2 1.1.4 2.3.6 3.6.6.6 0 1 .4 1 1V20c0 .6-.4 1-1 1A17 17 0 013 4c0-.6.4-1 1-1h3.5c.6 0 1 .4 1 1 0 1.3.2 2.5.6 3.6.1.3 0 .7-.2 1z" fill="#f6b22d"/></svg>(555) 014 2278</div>
  <div><svg viewBox="0 0 15 11"><rect width="15" height="11" rx="1" fill="#f6b22d"/><path d="M0 0l7.5 6L15 0" stroke="#151515" stroke-width="1.5" fill="none"/></svg>hello@pineharbour.test</div>
  <div><svg viewBox="0 0 24 24"><path d="M12 2a7 7 0 00-7 7c0 5 7 13 7 13s7-8 7-13a7 7 0 00-7-7zm0 9.5A2.5 2.5 0 1112 6a2.5 2.5 0 010 5.5z" fill="#f6b22d"/></svg>12 Wharf Road, Pine Bay</div>
</div>
<div class="abs" style="left:108px;top:4960px;font-size:11px;color:var(--footer-text)">Copyright © 2024 Pine Harbour Removals. All Rights Reserved.</div>
<div class="abs" style="left:880px;top:4960px;font-size:11px;color:var(--footer-text)">Terms &amp; Conditions | &nbsp;Privacy Policy</div>

</body>
</html>
```